Your Harbor Agent Website Design

Creative Brief: Website Design for Your Harbor Agent
- Project Overview: Design a website for our new brand, "Your Harbor Agent". Your Harbor Agent is a service that matches clients with the perfect realtor. The primary function of this site is to serve as a lead generation hub, to generate leads of people who are looking to either buy or sell their house and need a great realtor. The site needs to have a very clean, modern design using sites like Tallyquest, Brickwell, Lantern, and Vexomill as an example. The site also needs to have a primary lead capture capability through a multi-step form or questionnaire that indicates if they are buying or selling, and depending on that selection, creates two different flows.

Target Audience:
- Homebuyers and sellers in the Denver area
- Individuals looking for high-quality realtor services
- Users seeking a seamless and professional online & home buying/selling experience

Objectives:
- Create a visually appealing, modern website with a strong emphasis on lead generation.
- Design advanced, multi-step forms for efficient lead capture.
- Ensure the website is user-friendly and optimized for both desktop and mobile devices.

Pages to Design:
Home Page:
- Engaging hero section with a clear call to action and the ability to enter the form flow
- Brief introduction to Your Harbor Agent and its unique value proposition
- Key features & benefits of being matched with a realtor by Your Harbor Agent
- Testimonials and success stories
- Lead capture form

About Page:
- Overview of Your Harbor Agent’s mission and values
- Professional and trust-building imagery

How it Works Page:
- Step-by-step explanation of the matching process (complete the form and we will match you with a realtor)
- Visual aids (icons, graphics) to simplify complex information
- Customer journey map from inquiry to successful match & sale of home
- Lead capture form

Contact Us Page:
- Simple and accessible contact form
- Contact details
- Call to action for immediate inquiries

Blog Template:
- Clean, easy-to-read layout for blog posts, primarily location/neighborhood guides as well as standard blogs
- Sidebar for recent posts, categories, and tags
- Social sharing buttons
- Lead capture form embedded within blog posts

Design Style:
- Modern and professional with a focus on usability
- Clean lines and intuitive navigation
- Use of curved corners and minimal straight lines for a sleek look
- Incorporation of graphic design elements, potentially including 3D and isomorphic design
- Inspired by sites like Tallyquest, Brickwell, Lantern, and Vexomill
Consistent color scheme and typography

Visual References:
- Tallyquest: For its professional and corporate look
- Brickwell and Lantern: For their user-friendly interfaces and modern design
- Vexomill: For its clean and functional layout

Target Market(s)

- Homebuyers and sellers in the Denver area, Individuals looking for high-quality realtor services, Users seeking a seamless and professional home buying/selling experience

Industry/Entity Type

Real Estate

Number of Pages Required

5+ page

Requirements
Must have
• Fully designed website with lead capture functionality based on brief
Nice to have
• Designed in Figma, Starting / Placeholder copy

```html
<!DOCTYPE html>
<html lang="en">
<head>
<meta charset="utf-8">
<title>Your Harbor Agent</title>
<link href="https://fonts.googleapis.com/css2?family=Barlow+Condensed:wght@400;500;600&family=DM+Sans:wght@400;500;700&display=swap" rel="stylesheet">
<style>
:root{
  --blue:#1877f2;
  --blue-soft:#eaf3fe;
  --navy:#0e2a47;
  --band:#0b3a68;
  --text:#3c4a5c;
  --muted:#6b7687;
  --line:#dfe4ea;
  --white:#ffffff;
  --star:#f6b92b;
}
*{box-sizing:border-box;margin:0;padding:0}
html,body{width:1200px;height:4389px;overflow:hidden}
body{position:relative;background:var(--white);font-family:"DM Sans",sans-serif;color:var(--text)}
.abs{position:absolute}
.display{font-family:"Barlow Condensed",sans-serif;font-weight:500;color:var(--navy);letter-spacing:-0.5px}
.accent{color:var(--blue)}
.btn{position:absolute;display:flex;align-items:center;justify-content:center;background:var(--blue);color:var(--white);border-radius:30px;font-size:12px;font-weight:700;box-shadow:0 8px 18px rgba(24,119,242,.28)}
.photo{position:absolute}

/* nav */
.hero-bg{left:0;top:0;width:1200px;height:588px;background:linear-gradient(180deg,#fff 0%,#eef5fe 100%)}
.logo{font-family:"Barlow Condensed",sans-serif;font-weight:500;color:var(--blue);font-size:30px}
.nav{left:418px;top:43px;display:flex;gap:34px;font-size:12px;color:var(--navy)}
.lang{left:985px;top:43px;font-size:12px;color:var(--navy);display:flex;align-items:center;gap:6px}
.lang i{display:inline-block;width:18px;height:12px;background:#2b4da0;border-radius:2px}

.hero-title{left:140px;top:165px;font-size:66px;line-height:67px}
.hero-sub{left:142px;top:384px;width:270px;font-size:14px;line-height:22px}

.stat{top:684px;width:240px;text-align:center}
.stat b{display:block;font-family:"Barlow Condensed",sans-serif;font-weight:400;font-size:56px;line-height:60px;color:var(--navy)}
.stat span{font-size:11px;color:var(--navy)}
.rule{left:235px;top:796px;width:732px;height:1px;background:var(--line)}

.sell-title{left:235px;top:862px;font-size:44px;line-height:44px}
.sell-sub{left:236px;top:973px;font-size:11px;color:var(--navy)}
.sell-sub u{font-weight:700}

.step{top:1028px;width:227px;height:322px;background:var(--white);border:1px solid #eef1f5;border-radius:18px;box-shadow:0 10px 30px rgba(14,42,71,.06);text-align:center}
.step .tag{position:absolute;left:22px;top:20px;font-size:10px;color:var(--muted)}
.step .ic{position:absolute;left:70px;top:54px;width:86px;height:86px;border-radius:50%;background:var(--blue);display:flex;align-items:center;justify-content:center}
.step h3{position:absolute;left:0;right:0;top:152px;font-size:16px;line-height:20px;color:var(--navy);font-weight:700}
.step p{position:absolute;left:20px;right:20px;top:216px;font-size:10.5px;line-height:16px;color:var(--muted)}

.about-bg{left:600px;top:1432px;width:600px;height:469px;background:var(--blue-soft)}
.about-title{left:679px;top:1502px;font-size:44px;line-height:44px}
.about-text{left:679px;width:315px;font-size:11px;line-height:20px;color:var(--text)}

.quote-title{left:0;width:1200px;top:1980px;text-align:center;font-size:44px;line-height:46px}
.quote{top:2114px;width:350px;height:251px;background:var(--white);border-radius:12px;box-shadow:0 10px 36px rgba(14,42,71,.08)}
.quote .mark{position:absolute;left:18px;top:36px;width:42px;height:42px;border-radius:50%;background:var(--blue);color:#fff;font-family:Georgia,serif;font-size:38px;line-height:50px;text-align:center;font-weight:700}
.quote h4{position:absolute;left:72px;top:34px;width:230px;font-size:14.5px;line-height:18px;color:var(--navy)}
.quote p{position:absolute;left:72px;top:86px;width:230px;font-size:10.5px;line-height:15.5px;color:var(--muted)}
.quote .who{position:absolute;left:72px;top:180px;font-size:10px;color:var(--navy)}
.quote .stars{position:absolute;left:72px;top:198px;color:var(--star);font-size:17px;letter-spacing:1px}
.dots{left:571px;top:2397px;display:flex;gap:8px}
.dots i{width:9px;height:9px;border-radius:50%;border:1px solid var(--blue)}
.dots i.on{background:var(--blue)}

.cash{left:0;top:2476px;width:1200px;height:209px;background:var(--blue)}
.cash h2{position:absolute;left:235px;top:75px;font-family:"Barlow Condensed",sans-serif;font-weight:500;font-size:38px;color:#fff}
.cash .field{position:absolute;left:546px;top:75px;width:419px;height:44px;background:#fff;border-radius:3px}
.cash .field span{position:absolute;left:22px;top:14px;font-size:11px;color:var(--muted)}
.cash .field b{position:absolute;right:5px;top:5px;width:116px;height:34px;background:var(--band);color:#fff;font-size:10px;display:flex;align-items:center;justify-content:center;border-radius:2px}
.cash .checks{position:absolute;left:548px;top:140px;display:flex;gap:16px;font-size:10px;color:#fff}
.cash .checks span{display:flex;align-items:center;gap:5px}

.buy-label{left:0;width:1200px;top:2756px;text-align:center;font-family:"Barlow Condensed",sans-serif;font-size:27px;letter-spacing:3px;color:var(--blue)}
.buy-card{left:235px;top:2852px;width:730px;height:417px;border-radius:22px;background:linear-gradient(135deg,#f4f9ff,#e7f1fd)}
.buy-title{left:278px;top:2918px;font-size:38px;line-height:40px}
.buy-text{left:279px;top:3052px;width:300px;font-size:11.5px;line-height:18px;color:var(--text)}

.contact-band{left:0;top:3345px;width:1200px;height:449px;background:var(--band)}
.contact-label{left:0;width:1200px;top:3402px;text-align:center;font-family:"Barlow Condensed",sans-serif;font-size:15px;letter-spacing:2px;color:#5ea2f8}
.contact-title{left:0;width:1200px;top:3425px;text-align:center;font-size:44px;color:#fff}
.contact-card{left:235px;top:3499px;width:730px;height:383px;background:#fff;box-shadow:0 10px 40px rgba(14,42,71,.1)}
.contact-side{left:235px;top:3499px;width:256px;height:383px;background:var(--blue)}
.contact-side h4{position:absolute;left:26px;top:36px;color:#fff;font-size:14px}
.cline{position:absolute;left:26px;display:flex;gap:12px;align-items:flex-start;color:#fff}
.cline small{display:block;font-size:7.5px;letter-spacing:.4px}
.cline b{font-size:14px;font-weight:500}
.cline em{font-style:normal;font-size:9.5px}
.form-q{left:528px;top:3532px;font-size:14px;font-weight:700;color:var(--navy)}
.fld{position:absolute;width:198px;height:34px;border:1px solid var(--line);border-radius:3px;font-size:9.5px;color:var(--navy);padding:11px 14px}
.fld.sel{border-color:var(--blue)}
.fld .radio{position:absolute;right:12px;top:11px;width:11px;height:11px;border-radius:50%;background:#e3ecf7}
.fld.sel .radio{background:var(--blue);box-shadow:0 0 0 2px #d9e8fd}
.area{position:absolute;left:527px;top:3705px;width:408px;height:94px;border:1px solid var(--line);border-radius:3px}

.foot-logo{left:140px;top:3966px;font-size:30px}
.social{left:148px;top:4019px;display:flex;gap:22px}
.social i{width:14px;height:14px;border-radius:50%;background:var(--navy)}
.fcol{top:3970px}
.fcol h5{font-family:"Barlow Condensed",sans-serif;font-weight:500;font-size:19px;color:var(--navy);margin-bottom:12px}
.fcol li{list-style:none;font-size:11px;line-height:22.6px;color:var(--text)}
.app{left:140px;top:4204px;width:450px;height:76px;border:1px solid #d9e6f7;border-radius:12px}
.app span{position:absolute;left:26px;top:28px;font-size:14px;font-weight:500;color:var(--navy)}
.app i{position:absolute;top:20px;width:134px;height:38px;background:#0b0b0b;border-radius:6px}
.help{left:609px;top:4204px;width:450px;height:76px;background:#dcebfd;border-radius:12px}
.help span{position:absolute;left:32px;top:28px;font-size:14px;font-weight:500;color:var(--navy)}
.help b{position:absolute;left:272px;top:20px;width:160px;height:38px;background:var(--blue);color:#fff;border-radius:5px;font-size:11px;font-weight:500;display:flex;align-items:center;justify-content:center}
.bottom-rule{left:140px;top:4322px;width:919px;height:2px;background:#9db7d6}
.copy{left:0;width:1200px;top:4355px;text-align:center;font-size:10px;color:var(--navy)}
</style>
</head>
<body>

<div class="abs hero-bg"></div>
<header>
  <div class="abs logo" style="left:140px;top:30px">Harbor Agent</div>
  <nav class="abs nav"><span>About Harbor Agent</span><span>How it works</span><span>Blogs</span><span>Contact Us</span></nav>
  <a class="btn" style="left:864px;top:33px;width:103px;height:35px">Sign up</a>
  <div class="abs lang"><i></i>English ▾</div>
</header>

<section>
  <h1 class="abs display hero-title">Find the<br>Perfect <span class="accent">Realtor</span><br><span class="accent">in Denver</span></h1>
  <p class="abs hero-sub">Helping you buy or sell your home with ease and confidence</p>
  <a class="btn" style="left:140px;top:443px;width:174px;height:43px">Find Your Realtor</a>
  <div class="photo" role="img" aria-label="Illustrated city skyline with a man on a phone call seated beside a large phone showing a video home walkthrough" style="left:452px;top:128px;width:656px;height:528px;background:radial-gradient(ellipse at 60% 55%,#dbe9fb 0%,#eef5fe 60%,rgba(238,245,254,0) 78%)"></div>
</section>

<section>
  <div class="abs stat" style="left:279px"><b>2,000+</b><span>Happy Homebuyers and sellers</span></div>
  <div class="abs stat" style="left:514px"><b>1500+</b><span>High-quality Realtor</span></div>
  <div class="abs stat" style="left:714px"><b>4.5 <span style="color:var(--star);font-size:40px">★</span></b><span>Customer Rating</span></div>
  <div class="abs rule"></div>
</section>

<section>
  <h2 class="abs display sell-title">Sell to <span class="accent">Our Denver<br>Realtor</span>. Skip the hard parts.</h2>
  <a class="btn" style="left:791px;top:905px;width:174px;height:41px">Get Started Now</a>
  <p class="abs sell-sub">We make selling your home fast, easy, and stress-free. <u>See how it works.</u></p>

  <div class="abs step" style="left:235px">
    <span class="tag">STEP 01</span>
    <div class="ic"><svg width="42" height="42" viewBox="0 0 24 24" fill="none" stroke="#fff" stroke-width="1.5" stroke-linecap="round" stroke-linejoin="round"><path d="M3 11l4-4 4 3 3-3 4 1 3 3-6 7-4-3-3 2z"/><path d="M9 14l2 2M12 12l2 2"/></svg></div>
    <h3>Get Matched<br>with a Realtor</h3>
    <p>Based on your information, we will match you with top-rated realtors in Denver who specialize in your needs. Our algorithm ensures you get the best possible match.</p>
  </div>
  <div class="abs step" style="left:488px">
    <span class="tag">STEP 02</span>
    <div class="ic"><svg width="40" height="40" viewBox="0 0 24 24" fill="none" stroke="#fff" stroke-width="1.5" stroke-linecap="round" stroke-linejoin="round"><rect x="4" y="4" width="16" height="12" rx="2"/><path d="M8 20l3-4M8 8h8M8 12h5"/></svg></div>
    <h3>Connect with<br>Your Realtor</h3>
    <p>Receive an introduction to your dedicated realtor. You can schedule a call or meeting at your convenience to discuss your goals and start your home buying or selling journey.</p>
  </div>
  <div class="abs step" style="left:738px">
    <span class="tag">STEP 03</span>
    <div class="ic"><svg width="40" height="40" viewBox="0 0 24 24" fill="none" stroke="#fff" stroke-width="1.5" stroke-linecap="round" stroke-linejoin="round"><path d="M3 11l9-7 9 7"/><path d="M5 10v10h14V10"/><path d="M10 20v-5h4v5"/></svg></div>
    <h3>Successfully Buy or<br>Sell Your Home</h3>
    <p>Work closely with your realtor to navigate the buying or selling process. From viewing homes to closing the deal, we ensure a smooth and successful experience.</p>
  </div>
</section>

<section>
  <div class="photo" role="img" aria-label="Photograph of a smiling family with two children and a dog standing indoors by a window" style="left:0;top:1432px;width:600px;height:469px;background:linear-gradient(90deg,#9fb18c 0%,#cdbfae 18%,#d8d2c8 55%,#b9b2a8 100%)"></div>
  <div class="abs about-bg"></div>
  <div class="photo" role="img" aria-label="Faint line drawing of city towers" style="left:1058px;top:1585px;width:142px;height:333px;background:linear-gradient(180deg,rgba(173,196,224,0) 0%,rgba(173,196,224,.35) 100%)"></div>
  <h2 class="abs display about-title">About Your<br><span class="accent">Harbor Agent</span></h2>
  <p class="abs about-text" style="top:1605px">Lorem ipsum dolor sit amet, consectetur adipiscing elit. Donec vitae fringilla mauris. Mauris eleifend ipsum sed dui pharetra tincidunt. Nam sit amet ligula lectus. Phasellus felis justo, consequat ac nisl ut, venenatis efficitur nisl. Quisque rhoncus sagittis justo dignissim vehicula. Fusce tincidunt metus aliquet mauris interdum elementum.</p>
  <p class="abs about-text" style="top:1740px">Lorem ipsum dolor sit amet, consectetur adipiscing elit. Donec vitae fringilla mauris. Mauris eleifend ipsum sed dui pharetra tincidunt. Nam sit amet ligula lectus. Phasellus felis justo, consequat ac nisl ut, venenatis efficitur nisl.</p>
</section>

<section>
  <h2 class="abs display quote-title">Join <span class="accent">Your Harbor Agent customers</span><br>who moved without the hassle</h2>
  <div class="abs quote" style="left:235px"><span class="mark">“</span><h4>The process couldn’t have been easier</h4><p>Your Harbor Agent made buying our first home a breeze. They matched us with an amazing realtor who understood our needs perfectly. We couldn’t be happier with our new home!”</p><span class="who">-Name of Buyer</span><span class="stars">★★★★★</span></div>
  <div class="abs quote" style="left:614px"><span class="mark">“</span><h4>The process couldn’t have been easier</h4><p>Your Harbor Agent made buying our first home a breeze. They matched us with an amazing realtor who understood our needs perfectly. We couldn’t be happier with our new home!”</p><span class="who">-Name of Buyer</span><span class="stars">★★★★★</span></div>
  <div class="abs dots"><i class="on"></i><i></i><i></i><i></i></div>
</section>

<section class="abs cash">
  <h2>Get a cash offer now!</h2>
  <div class="field"><span>Enter your address here..</span><b>GET STARTED</b></div>
  <div class="checks">
    <span><svg width="11" height="11" viewBox="0 0 12 12" fill="none" stroke="#fff"><circle cx="6" cy="6" r="5"/><path d="M3.5 6l2 2 3-4"/></svg>Good Realtors</span>
    <span><svg width="11" height="11" viewBox="0 0 12 12" fill="none" stroke="#fff"><circle cx="6" cy="6" r="5"/><path d="M3.5 6l2 2 3-4"/></svg>No Fees</span>
    <span><svg width="11" height="11" viewBox="0 0 12 12" fill="none" stroke="#fff"><circle cx="6" cy="6" r="5"/><path d="M3.5 6l2 2 3-4"/></svg>No Repairs</span>
  </div>
</section>

<section>
  <div class="abs buy-label">ALSO BUYING A HOME?</div>
  <div class="abs buy-card"></div>
  <h2 class="abs display buy-title">Find Your <span class="accent">Dream<br>Home</span> With Ease And<br>Confidence.</h2>
  <p class="abs buy-text">Avoid double mortgages and moves when you sell and buy a home with Your Harbor Agent.</p>
  <a class="btn" style="left:278px;top:3108px;width:172px;height:43px">Browse Our Homes</a>
  <div class="photo" role="img" aria-label="Cut-out photograph of a happy family of three pointing toward the text, with a faint skyline behind" style="left:605px;top:2788px;width:341px;height:537px;background:radial-gradient(ellipse at 50% 50%,#b8cbe0 0%,#d6e3f1 45%,rgba(231,241,253,0) 75%)"></div>
</section>

<section>
  <div class="abs contact-band"></div>
  <div class="abs contact-label">CONTACT INFORMATION</div>
  <h2 class="abs display contact-title">Your Harbor Agent Contact</h2>
  <div class="abs contact-card"></div>
  <div class="abs contact-side">
    <h4>Let’s Get Started</h4>
    <div class="cline" style="top:80px"><svg width="20" height="20" viewBox="0 0 24 24" fill="none" stroke="#fff" stroke-width="1.5"><path d="M5 3h4l2 5-3 2a11 11 0 006 6l2-3 5 2v4a2 2 0 01-2 2A17 17 0 013 5a2 2 0 012-2z"/></svg><div><small>CALL US TODAY:</small><b>(555) 014-2290</b></div></div>
    <div class="cline" style="top:126px"><svg width="20" height="16" viewBox="0 0 24 18" fill="none" stroke="#fff" stroke-width="1.5"><rect x="1" y="1" width="22" height="16" rx="1"/><path d="M1 2l11 8 11-8"/></svg><div><small>EMAIL ADDRESS:</small><em>hello@yourharboragent.com</em></div></div>
  </div>
  <div class="photo" role="img" aria-label="Photograph of a white house with columns and a pool deck" style="left:235px;top:3683px;width:256px;height:199px;background:linear-gradient(180deg,#8fc4ef 0%,#e9eef2 55%,#c9a6c7 100%)"></div>
  <div class="abs form-q">Are you looking to buy or sell a home?</div>
  <div class="fld" style="left:527px;top:3569px">Buying<span class="radio"></span></div>
  <div class="fld sel" style="left:737px;top:3569px">Selling<span class="radio"></span></div>
  <div class="fld" style="left:527px;top:3615px">First Name</div>
  <div class="fld" style="left:737px;top:3615px">Last Name</div>
  <div class="fld" style="left:527px;top:3661px">Email Addresst</div>
  <div class="fld" style="left:737px;top:3661px">Last Name</div>
  <div class="area"></div>
  <a class="btn" style="left:808px;top:3819px;width:126px;height:34px;font-weight:500">Submit Now</a>
</section>

<footer>
  <div class="abs logo foot-logo">Harbor Agent</div>
  <div class="abs social"><i></i><i></i><i></i><i></i></div>
  <div class="abs fcol" style="left:373px"><h5>About Us</h5><ul><li>Company</li><li>Press</li><li>News</li><li>Contact</li><li>Investors</li><li>Careers</li><li>Brokerages</li></ul></div>
  <div class="abs fcol" style="left:515px;width:190px"><h5>Terms &amp; Privacy</h5><ul><li>Trust and safety</li><li>Terms of service</li><li>Privacy policy</li><li>Notice at collection</li><li style="line-height:16px;padding-top:3px">Do not sell or share my personal information</li></ul></div>
  <div class="abs fcol" style="left:766px"><h5>Products</h5><ul><li>Browse Homes</li><li>Sell your home</li><li>Mortgage calculator</li><li>home sale calculator</li><li>stories</li><li>reviews</li></ul></div>
  <div class="abs fcol" style="left:953px"><h5>Partners</h5><ul><li>Agents</li><li>builders</li><li>work with a builder</li><li>Vendors</li></ul></div>

  <div class="abs app"><span>Get The App</span><i style="left:150px"></i><i style="left:294px"></i></div>
  <div class="abs help"><span>Still have a questions?</span><b>Visit the help center</b></div>
  <div class="abs bottom-rule"></div>
  <div class="abs copy">©2024 Your Harbor Agent. All Rights Reserved.</div>
</footer>

</body>
</html>
```